Business Card for my Photography/Video Business

I would like the card to say Event Photographer and Videographer. I like the Black and Gold look to it as well but open to other options. I don't want it to be super vibrant or colorful. Simple, elegant and professional

```html
<!DOCTYPE html>
<html lang="en">
<head>
<meta charset="utf-8">
<title>Lumen Frame Business Card</title>
<link rel="stylesheet" href="https://fonts.googleapis.com/css2?family=Lato:wght@400;700&display=swap">
<style>
  :root {
    --bg-top: #3c3c3c;
    --bg-bottom: #2a2a2a;
    --card-white: #ffffff;
    --card-black: #1c1c1c;
    --card-black-light: #2e2e2e;
    --gold: #c9a545;
    --gold-deep: #b48f33;
    --ink: #1a1a1a;
    --ink-soft: #f1f1f1;
  }
  * { margin: 0; padding: 0; box-sizing: border-box; }
  html, body { width: 1200px; height: 900px; overflow: hidden; }
  body {
    background: radial-gradient(ellipse at 55% 40%, var(--bg-top), var(--bg-bottom));
    font-family: "Lato", sans-serif;
    position: relative;
  }
  .card {
    position: absolute;
    top: 302px;
    width: 520px;
    height: 296px;
    overflow: hidden;
    box-shadow: 0 14px 30px rgba(0,0,0,0.45);
  }
  .card-front { left: 50px; background: var(--card-white); }
  .card-back {
    left: 630px;
    background: linear-gradient(135deg, var(--card-black-light), var(--card-black) 70%);
  }

  /* Brand lockup */
  .brand { position: absolute; display: flex; align-items: center; gap: 14px; }
  .brand-dot {
    width: 62px; height: 62px; border-radius: 50%;
    background: var(--gold);
    flex: none;
  }
  .brand-name {
    font-weight: 700;
    font-size: 38px;
    letter-spacing: 3px;
    color: var(--gold);
    text-transform: uppercase;
    white-space: nowrap;
  }
  .card-front .brand { left: 30px; top: 26px; }
  .card-back .brand { left: 96px; top: 100px; }
  .card-back .brand-dot { width: 72px; height: 72px; }
  .card-back .brand-name { font-size: 40px; }

  /* Front details */
  .rule {
    position: absolute;
    left: 52px; right: 34px; top: 150px;
    height: 1.5px; background: var(--gold);
  }
  .person { position: absolute; right: 40px; top: 104px; text-align: right; }
  .person-name { font-weight: 700; font-size: 22px; color: var(--gold); line-height: 1.1; }
  .person-role { font-size: 14px; color: var(--ink); line-height: 1.3; }

  .contacts { position: absolute; left: 32px; top: 164px; list-style: none; }
  .contacts li {
    display: flex; align-items: center; gap: 7px;
    font-size: 13px; color: var(--ink); line-height: 17px;
  }
  .contacts svg { width: 11px; height: 11px; flex: none; }

  .address {
    position: absolute; right: 40px; top: 196px;
    text-align: right; font-size: 15px; color: var(--ink); line-height: 1.25;
  }

  .footer-band { position: absolute; left: 0; bottom: 0; width: 520px; height: 44px; }
  .footer-web {
    position: absolute; right: 40px; bottom: 9px;
    font-size: 14px; color: var(--ink-soft); letter-spacing: 0.5px;
  }

  .back-web {
    position: absolute; left: 110px; top: 218px;
    font-size: 14px; color: var(--ink-soft); letter-spacing: 0.8px;
  }
</style>
</head>
<body>

  <section class="card card-front">
    <div class="brand">
      <span class="brand-dot"></span>
      <span class="brand-name">Lumen Frame</span>
    </div>

    <div class="person">
      <div class="person-name">Daniel Hale</div>
      <div class="person-role">Manager</div>
    </div>
    <div class="rule"></div>

    <ul class="contacts">
      <li>
        <svg viewBox="0 0 12 12"><path fill="#c9a545" d="M2.5 1l2 2.2-1 1.2c.7 1.5 1.8 2.6 3.2 3.2l1.2-1 2.1 2-1.2 1.9C5.5 10.5 1.5 6.5 1 2.3z"/></svg>
        512 555 0142
      </li>
      <li>
        <svg viewBox="0 0 12 12"><rect x="3" y="0.5" width="6" height="11" rx="1" fill="#c9a545"/><rect x="4" y="2" width="4" height="6.5" fill="#ffffff"/></svg>
        512 555 0143
      </li>
      <li>
        <svg viewBox="0 0 12 12"><rect x="0.5" y="2" width="11" height="8" fill="#c9a545"/><path d="M0.5 2l5.5 4.5L11.5 2" fill="none" stroke="#ffffff" stroke-width="1"/></svg>
        hello@lumenframe.com
      </li>
    </ul>

    <div class="address">48 Cedar Row<br>Austin, TX 78701</div>

    <svg class="footer-band" viewBox="0 0 520 44" aria-hidden="true">
      <rect x="0" y="20" width="200" height="24" fill="#c9a545"/>
      <path d="M150 44 C175 44 180 6 215 6 L520 6 L520 44 Z" fill="#1f1f1f"/>
      <path d="M150 44 C175 44 180 6 215 6" fill="none" stroke="#ffffff" stroke-width="2"/>
    </svg>
    <div class="footer-web">www.lumenframe.com</div>
  </section>

  <section class="card card-back">
    <div class="brand">
      <span class="brand-dot"></span>
      <span class="brand-name">Lumen Frame</span>
    </div>
    <div class="back-web">www.lumenframe.com</div>
  </section>

</body>
</html>
```